postcard for Real Estate Agent that sells homes for less than any other agents

My company sells houses for a fraction of what others charge. I have most of the verbiage but I am open to ideas.
Our post card will be 6.25 x 9
We need an image that goes with our words and draws people to take a look
We are playful at the same time very serious about the money we will save our clients. In the past our message has been received as too good to be true. Our old message was "save $6000* when you list with us" We think the "*" was causing people to think their was a catch. Other agents will tell people that we will not do what they will do and that is why they must charge more. We are a full service agency and we will generally do everything that other agents will do and in many cases we will do more than other agents. We are changing this industry and need our message to get to every person that is thinking of selling their home

Target Market(s)

People who want to list their home for sale

Industry/Entity Type

Real Estate Agent

Requirements
Must have
• Image that makes people read the message

```html
<!DOCTYPE html>
<html lang="en">
<head>
<meta charset="utf-8">
<title>Homeward Keys Postcard</title>
<link href="https://fonts.googleapis.com/css2?family=Arimo:wght@700&family=Archivo+Black&display=swap" rel="stylesheet">
<style>
  :root {
    --navy: #1b4888;
    --yellow: #fff200;
    --sky: #8fb6dc;
    --white: #ffffff;
    --green: #a8d470;
    --ink: #1d3f78;
  }
  * { margin: 0; padding: 0; box-sizing: border-box; }
  html, body { width: 1200px; height: 800px; overflow: hidden; background: var(--white); }
  .postcard { position: relative; width: 1200px; height: 800px; overflow: hidden; background: var(--white); font-family: "Arimo", Arial, sans-serif; font-weight: 700; color: var(--white); }
  .panel { position: absolute; inset: 0; }
  .headline { position: absolute; left: 62px; top: 40px; }
  .headline p { font-size: 51px; line-height: 58px; letter-spacing: -0.2px; }
  .headline .shout { font-family: "Archivo Black", "Arial Black", sans-serif; font-size: 81px; line-height: 86px; color: var(--yellow); letter-spacing: 0.5px; margin: 0 0 0; }
  .teaser { position: absolute; left: 62px; top: 324px; font-family: "Archivo Black", "Arial Black", sans-serif; font-size: 30px; line-height: 38px; color: var(--sky); letter-spacing: 0.8px; }
  .teaser span { color: var(--white); font-size: 31px; }
  .ideas { position: absolute; left: 345px; top: 377px; display: grid; grid-template-columns: 220px 220px; row-gap: 5px; list-style: none; font-size: 17.5px; }
  .ideas li { position: relative; padding-left: 21px; line-height: 21px; }
  .ideas li::before { content: ""; position: absolute; left: 0; top: 5px; border-left: 10px solid var(--sky); border-top: 5.5px solid transparent; border-bottom: 5.5px solid transparent; }
  .promise { position: absolute; left: 355px; top: 540px; font-size: 29px; line-height: 37px; color: var(--sky); letter-spacing: 0.4px; }
  .call { position: absolute; left: 358px; top: 626px; font-size: 26px; }
  .phone { position: absolute; left: 356px; top: 660px; font-family: "Archivo Black", "Arial Black", sans-serif; font-size: 48px; line-height: 56px; color: var(--sky); letter-spacing: 1px; }
  .web { position: absolute; left: 358px; top: 722px; font-size: 29px; color: var(--green); }
  .thinker { position: absolute; left: 20px; top: 395px; width: 320px; height: 405px; border-radius: 140px 140px 0 0; background: linear-gradient(180deg, #c99b7e 0%, #b88a70 35%, #2a2f3c 55%, #1c2130 100%); }
  .yard-photo { position: absolute; left: 812px; top: 130px; width: 378px; height: 378px; border-radius: 50%; border: 7px solid var(--white); background: radial-gradient(circle at 60% 35%, #e23038 0%, #c9c2b5 25%, #7a5a4a 55%, #4d7a33 80%, #3e6a2a 100%); }
  .brand { position: absolute; left: 826px; top: 665px; display: flex; align-items: center; gap: 12px; color: var(--ink); font-family: "Archivo Black", "Arial Black", sans-serif; font-size: 33px; line-height: 40px; white-space: nowrap; }
  .brand i { display: block; width: 30px; height: 30px; background: var(--ink); }
</style>
</head>
<body>
<div class="postcard">
  <svg class="panel" width="1200" height="800" viewBox="0 0 1200 800" aria-hidden="true">
    <polygon points="0,0 1168,0 718,800 0,800" fill="var(--navy)"/>
  </svg>

  <div class="headline">
    <p>You’d have to be</p>
    <p class="shout">Bat $#@T CRAZY</p>
    <p>to give an agent $6000.00</p>
    <p>To put a sign in your yard.</p>
  </div>

  <p class="teaser">Look at what you can do with <span>$6000.00</span></p>

  <ul class="ideas">
    <li>Give it to your Kids</li><li>Build a fence</li>
    <li>Build a deck</li><li>Buy new clothes</li>
    <li>Landscape</li><li>Take a Vacation</li>
    <li>Pay off your car</li><li>Pay off student loan</li>
    <li>Buy New Carpet</li><li>Upgrade Appliances</li>
  </ul>

  <p class="promise">FULL SERVICE AGENCY AT A<br>FRACTION OF THE COST</p>
  <p class="call">Call Dana or Marcus at</p>
  <p class="phone">970.555.0142</p>
  <p class="web">www.HomewardKeys.com</p>

  <div class="thinker" role="img" aria-label="Photo of a thoughtful man in a dark suit, hand on chin, looking upward"></div>
  <div class="yard-photo" role="img" aria-label="Photo of a red For Sale sign in front of a house behind a green hedge"></div>

  <p class="brand"><i></i>Homeward Keys</p>
</div>
</body>
</html>
```